VelnoraTek Bright IT Consultancy
All Stationary + ESignaure + Powerpoint Template
Simple
Tomás Barrena Ollé
President & CEO
3er Cjon Calle Fresal 57
Las Brisas, Coyoacán
México DF, 07215
See additional comments
tomas.barrena@velnoratek.mx
www.velnoratek.com.mx
I dont have a permanent local phone number yet, so I dont want to give an informal impression about the company, so Designers I need your creativite to avoid that impression something as simple as "cell&phone" but with all your experience and creativity, an special cell+phone logo for example. Other request is a clean, simple, modern, corporate and professional material.
Go Bright...Go Sky
Go Sky...& Connect
Share...& Succed
Logo Velno
Logo Velno 2
Logo 3
Logo 4
This is an example of standard bullets and numbers in a powerpoint presentation

```html
<!DOCTYPE html>
<html lang="en">
<head>
<meta charset="utf-8">
<title>VelnoraTek Stationery Set</title>
<link href="https://fonts.googleapis.com/css2?family=Questrial&display=swap" rel="stylesheet">
<style>
  :root{
    --board:#e4e6e7;
    --paper:#ffffff;
    --ink:#3d4a55;
    --teal:#4a7389;
    --teal-soft:#c9d9e2;
    --olive:#8b8e5e;
    --slate:#5c6063;
    --label:#8d9296;
    --mark:#a9c2cf;
  }
  *{box-sizing:border-box;margin:0;padding:0}
  html,body{width:1200px;height:684px;overflow:hidden}
  body{background:var(--board);font-family:"Questrial",sans-serif;color:var(--ink);position:relative}
  .piece{position:absolute;background:var(--paper);box-shadow:0 1px 4px rgba(0,0,0,.12);overflow:hidden}
  .label{position:absolute;font-size:8px;color:var(--label);text-align:center;letter-spacing:.3px}
  .brand{display:flex;align-items:center;gap:4px;white-space:nowrap}
  .brand .dot{border-radius:50%;background:var(--teal);flex:none}
  .brand .name{color:var(--ink);font-weight:400;line-height:1}
  .tagline{color:var(--label);letter-spacing:1.5px;text-transform:uppercase}
  .faint-mark{position:absolute;border-radius:50%;background:var(--mark);opacity:.28}
  .contact{font-size:4.5px;line-height:1.5;color:var(--slate)}

  /* letterhead */
  .letterhead{left:36px;top:29px;width:401px;height:440px}
  .letterhead .brand{position:absolute;left:30px;top:42px}
  .letterhead .contact{position:absolute;left:248px;top:38px}
  .letterhead .faint-mark{left:300px;bottom:36px;width:110px;height:110px}

  /* folder */
  .folder{left:461px;top:29px;width:396px;height:440px}
  .folder .lockup{position:absolute;left:0;right:0;top:175px;display:flex;flex-direction:column;align-items:center;gap:6px}
  .folder .tagline{font-size:9px;margin-left:60px}

  /* small cards */
  .card{width:194px;height:56px}
  .card .brand{position:absolute;left:12px;top:12px}
  .card .contact{position:absolute;right:12px;top:12px;text-align:right}
  .card-back .brand{position:absolute;left:50%;top:50%;transform:translate(-50%,-50%)}
  .card-back .faint-mark{width:42px;height:42px;left:8px;top:7px}
  .card-teal{background:var(--teal)}
  .card-olive{background:var(--olive)}
  .card-slate{background:var(--slate)}
  .card-teal .name,.card-olive .name,.card-slate .name{color:#fff}
  .card-teal .dot,.card-olive .dot,.card-slate .dot{background:#fff}

  .bottom-card{width:144px;height:58px}
  .quad-card{width:100px;height:58px}

  /* compliment slip */
  .slip{left:197px;top:482px;width:295px;height:140px}
  .slip .brand{position:absolute;left:16px;top:14px}
  .slip .with{position:absolute;right:18px;bottom:12px;font-size:11px;color:var(--teal)}

  /* envelope */
  .envelope{left:533px;top:482px;width:320px;height:140px}
  .envelope .flap{position:absolute;left:0;top:0;width:320px;height:78px}
  .envelope .web{position:absolute;left:0;right:0;top:16px;text-align:center;font-size:12px;letter-spacing:2px;color:#fff}
</style>
</head>
<body>

<!-- Letterhead -->
<section class="piece letterhead">
  <div class="brand"><span class="dot" style="width:9px;height:9px"></span><span class="name" style="font-size:13px">VelnoraTek</span></div>
  <div class="contact">
    3er Cjon Calle Fresal 57<br>Las Brisas, Coyoacán<br>México DF, 07215<br>tomas.barrena@velnoratek.mx<br>www.velnoratek.com.mx
  </div>
  <div class="faint-mark" role="img" aria-label="Faint brand emblem"></div>
</section>
<div class="label" style="left:36px;top:474px;width:401px">Letter Head</div>

<!-- Presentation folder -->
<section class="piece folder">
  <div class="lockup">
    <div class="brand"><span class="dot" style="width:30px;height:30px"></span><span class="name" style="font-size:36px">VelnoraTek</span></div>
    <div class="tagline">Bright IT Consultancy</div>
  </div>
</section>
<div class="label" style="left:461px;top:474px;width:396px">Presentation Folder</div>

<!-- Right card fronts -->
<section class="piece card" style="left:900px;top:233px">
  <div class="brand"><span class="dot" style="width:6px;height:6px"></span><span class="name" style="font-size:9px">VelnoraTek</span></div>
  <div class="contact">Tomás Barrena Ollé<br>President &amp; CEO<br>tomas.barrena@velnoratek.mx<br>www.velnoratek.com.mx</div>
</section>
<div class="label" style="left:900px;top:292px;width:194px">Card Front A</div>

<section class="piece card" style="left:900px;top:336px">
  <div class="brand"><span class="dot" style="width:6px;height:6px"></span><span class="name" style="font-size:9px">VelnoraTek</span></div>
  <div class="contact">Tomás Barrena Ollé<br>President &amp; CEO<br>tomas.barrena@velnoratek.mx<br>www.velnoratek.com.mx</div>
</section>
<div class="label" style="left:900px;top:395px;width:194px">Card Front B</div>

<!-- Bottom-left cards -->
<section class="piece card bottom-card" style="left:29px;top:482px">
  <div class="brand"><span class="dot" style="width:6px;height:6px"></span><span class="name" style="font-size:9px">VelnoraTek</span></div>
  <div class="contact" style="top:30px">Tomás Barrena Ollé<br>President &amp; CEO</div>
</section>
<div class="label" style="left:29px;top:543px;width:144px">Business Card Front</div>

<section class="piece card card-back card-teal bottom-card" style="left:29px;top:562px">
  <div class="brand"><span class="dot" style="width:6px;height:6px"></span><span class="name" style="font-size:10px">VelnoraTek</span></div>
</section>
<div class="label" style="left:29px;top:623px;width:144px">Business Card Back</div>

<div class="label" style="left:197px;top:626px;width:295px">Compliment Slip</div>
<section class="piece slip">
  <div class="brand"><span class="dot" style="width:7px;height:7px"></span><span class="name" style="font-size:11px">VelnoraTek</span></div>
  <div class="with">With Compliments</div>
</section>

<!-- Envelope -->
<section class="piece envelope">
  <svg class="flap" viewBox="0 0 320 78" aria-hidden="true">
    <path d="M0 0H320V30Q300 78 160 78Q20 78 0 30Z" fill="var(--teal)"/>
  </svg>
  <div class="web">www.velnoratek.com.mx</div>
</section>
<div class="label" style="left:533px;top:626px;width:320px">Envelope</div>

<!-- Back options -->
<section class="piece card card-back quad-card" style="left:896px;top:478px">
  <div class="faint-mark" role="img" aria-label="Faint brand emblem"></div>
  <div class="brand" style="left:62px"><span class="name" style="font-size:8px">VelnoraTek</span></div>
</section>
<div class="label" style="left:896px;top:538px;width:100px">Back Option A</div>

<section class="piece card card-back card-olive quad-card" style="left:1004px;top:478px">
  <div class="brand"><span class="dot" style="width:5px;height:5px"></span><span class="name" style="font-size:8px">VelnoraTek</span></div>
</section>
<div class="label" style="left:1004px;top:538px;width:100px">Back Option B</div>

<section class="piece card card-back quad-card" style="left:896px;top:562px">
  <div class="faint-mark" role="img" aria-label="Faint brand emblem"></div>
  <div class="brand" style="left:62px"><span class="name" style="font-size:8px">VelnoraTek</span></div>
</section>
<div class="label" style="left:896px;top:622px;width:100px">Back Option C</div>

<section class="piece card card-back card-slate quad-card" style="left:1004px;top:562px">
  <div class="brand"><span class="dot" style="width:5px;height:5px"></span><span class="name" style="font-size:8px">VelnoraTek</span></div>
</section>
<div class="label" style="left:1004px;top:622px;width:100px">Back Option D</div>

</body>
</html>
```